Aircraft maintenance buisness card

I am an aircraft mechanic looking for a personal buisness card . I would like my name and a title of Aircraft Maintenance Manager . I would like a suttle picture of an aircraft and helicopter .

elegant and professional wtih my contact .

My name should be on the car and Aircraft Maintenance Manager under with my contact infor below .

i have attached some pictures but i am open to other pics and ideas . I would like a airliner or private jet and a helicopter in the picture . The Images should be suttle and not the main idea . I also uploaded a picture of a jet engine which is cool . Be creative and i will work with you to finalize something .
Updates

Project Deadline Extended
Reason: Looking for more variations . Very good so far but looiking for a bit more styles and i uploaded my logo that i purchased . Please use my logo and be creative with it . I like some variations of black card with maybe some pictures that i uploaded but i am open to ideas . Be creative and i will work with you .

Project Deadline Extended
Reason: Looking for more designs and variations . Not yet satisfied with the designs i have gotten .

Industry/Entity Type

Aviation

Contact Information for Business Card

Aircraft Maintenance Manager

Font styles to use
Serif

Colors

Designer to choose colors to be used in the design.

Requirements
Must have
• An aviation related Logo if possible incorporated in the card possibly
• My name
• Tiberio Malvade Furtunato
• 482 Pellow St.
• Brisford , VT
• 08519
• Email: Lwskyfixtech@mailvora.com
Nice to have
• Suttle Backround of a Private Jet or Airliner and a Helicopter .

```html
<!DOCTYPE html>
<html lang="en">
<head>
<meta charset="utf-8">
<title>Tiberio Malvade Furtunato – Business Card</title>
<link href="https://fonts.googleapis.com/css2?family=Cinzel:wght@400;500&display=swap" rel="stylesheet">
<style>
  :root {
    --stage: #3b3b3b;
    --card-dark: #2a2a2a;
    --accent-blue: #4c74c9;
    --ink-light: #f2f2f2;
    --frame-line: #e8e8e8;
  }
  * { margin: 0; padding: 0; box-sizing: border-box; }
  html, body {
    width: 1200px; height: 1000px; overflow: hidden;
    background: var(--stage);
    font-family: "Cinzel", serif;
  }
  .card {
    position: absolute;
    left: 220px;
    width: 760px;
    height: 434px;
    overflow: hidden;
  }
  .card-front { top: 42px; }
  .card-back { top: 520px; background: var(--card-dark); }

  .front-photo {
    width: 100%; height: 100%;
    background:
      radial-gradient(ellipse at 60% 60%, #d9d6cf 0%, #b9b5ad 30%, transparent 60%),
      linear-gradient(180deg, #1d1d22 0%, #3a3d4a 35%, #8a8c96 65%, #d8d6d0 100%);
  }

  .back-photo {
    position: absolute; inset: 0;
    background:
      radial-gradient(ellipse at 20% 62%, rgba(120,120,120,0.35) 0%, transparent 22%),
      radial-gradient(ellipse at 85% 75%, rgba(120,120,120,0.3) 0%, transparent 20%),
      linear-gradient(180deg, #2a2a2a 0%, #333 50%, #262626 100%);
  }

  .name-frame {
    position: absolute;
    left: 96px; top: 50px;
    width: 568px; height: 124px;
    border: 2px solid var(--frame-line);
    text-align: center;
    padding-top: 22px;
  }
  .holder-name {
    color: var(--accent-blue);
    font-size: 31px;
    font-weight: 400;
    letter-spacing: 1px;
    white-space: nowrap;
  }
  .holder-title {
    color: var(--ink-light);
    font-size: 19px;
    margin-top: 8px;
    letter-spacing: 0.5px;
  }

  .contact-list {
    position: absolute;
    left: 0; right: 0; top: 208px;
    text-align: center;
    color: var(--ink-light);
    font-size: 18px;
    line-height: 30px;
    letter-spacing: 1px;
    list-style: none;
  }
  .contact-label { color: var(--accent-blue); }
  .contact-list .address-label { margin-top: 14px; }
</style>
</head>
<body>
  <section class="card card-front">
    <div class="front-photo" role="img" aria-label="Photograph of a silver executive helicopter on an exhibition floor"></div>
  </section>

  <section class="card card-back">
    <div class="back-photo" role="img" aria-label="Faint dark photograph of an airliner on the apron with a ground crew member"></div>

    <div class="name-frame">
      <h1 class="holder-name">Tiberio Malvade Furtunato</h1>
      <p class="holder-title">Aircraft Maintenance Manager</p>
    </div>

    <ul class="contact-list">
      <li><span class="contact-label">P:</span> 000 111 222 333</li>
      <li><span class="contact-label">E:</span> Lwskyfixtech@mailvora.com</li>
      <li><span class="contact-label">W:</span> www.lwskyfix.com</li>
      <li class="address-label"><span class="contact-label">Address:</span></li>
      <li>482 Pellow St. Brisford , VT 08519</li>
    </ul>
  </section>
</body>
</html>
```